Pembrook Insurance Post Card

Specializing in “Towing & Transportation Insurance”
See our website at http://pembrookins-example.net/ for ideas on colors fonts etc.

Target Market(s)

Towing Companies

Font styles to use
Serif
Sans Serif

Requirements
Must have
• Specializing in “Towing & Transportation Insurance”
• Welcome to Pembrook Insurance:
• 2nd sentence (With our Agency, we work to make ourselves available to your business for when you need us most to keep your business moving forward.)
• 3rd Sentence: (Our customers were in mind when developing our agency and will continue to find new ways to make doing business with us easier.)
• We Offer: Change “Dealers Physical Damage” to “Auto Dealer Liability” & “Garage Liability” to “Garage Repair Liability”
• Our address: 718 Hollis Row NW, Suite F Decatur, AL 35988
• Email Address: PembrookInfo@velmarlink.example

```html
<!DOCTYPE html>
<html lang="en">
<head>
<meta charset="utf-8">
<title>Pembrook Insurance Post Card</title>
<link rel="stylesheet" href="https://fonts.googleapis.com/css2?family=Lato:wght@400;700&family=Lora:wght@400;700&family=Oswald:wght@600&display=swap">
<style>
  :root {
    --navy: #0e3566;
    --navy-deep: #0a2a52;
    --gold: #9b7437;
    --gold-light: #c4a066;
    --ink: #1d1d1d;
    --grey-panel: #dcdbdb;
    --paper: #ffffff;
    --stage: #e8e8e8;
  }
  * { margin: 0; padding: 0; box-sizing: border-box; }
  html, body { width: 1200px; height: 1200px; overflow: hidden; background: var(--stage); }
  .canvas { position: relative; width: 1200px; height: 1200px; }
  .card {
    position: absolute; left: 265px; width: 838px; height: 605px;
    background: var(--paper); overflow: hidden;
    transform: scale(0.8); transform-origin: 0 0;
    box-shadow: 0 6px 18px rgba(0,0,0,.18);
  }
  .card--front { top: 104px; }
  .card--back { top: 640px; }
  .card svg.shapes { position: absolute; inset: 0; }
  .abs { position: absolute; white-space: nowrap; }
  .serif { font-family: "Lora", Georgia, serif; }
  .sans { font-family: "Lato", Arial, sans-serif; }

  /* front */
  .hero-kicker { left: 45px; top: 34px; color: #fff; font-size: 31px; line-height: 37px; }
  .hero-title { left: 44px; top: 108px; color: #fff; font-size: 62px; font-weight: 700; letter-spacing: 1px; }
  .brand-name { color: #fff; font-size: 22px; letter-spacing: 2px; right: 32px; top: 58px; }
  .welcome-kicker { left: 584px; top: 206px; color: var(--gold); font-size: 32px; }
  .welcome-name { left: 540px; top: 246px; color: var(--navy); font-size: 23px; font-weight: 700; }
  .welcome-copy { left: 536px; top: 282px; width: 276px; font-size: 10.2px; line-height: 13px; color: var(--ink); white-space: normal; }
  .call-label { right: 50px; top: 430px; font-size: 27px; font-weight: 700; color: var(--ink); }
  .call-number { right: 46px; top: 466px; font-family: "Oswald", Impact, sans-serif; font-size: 36px; font-weight: 600; color: var(--gold); }
  .web-front { left: 568px; top: 561px; font-size: 13px; font-weight: 700; letter-spacing: 1.5px; color: var(--ink); }
  .truck-photo { left: 0; top: 362px; width: 525px; height: 230px;
    background: linear-gradient(100deg, #5b4a55 0%, #8a8a8e 35%, #e9e9ea 70%, #cfcfd1 100%); }

  /* back */
  .intro-panel { left: 0; top: 83px; width: 425px; height: 155px; background: var(--grey-panel); padding: 32px 60px 0 33px; font-size: 12.5px; line-height: 15.5px; color: var(--ink); white-space: normal; }
  .intro-panel p + p { margin-top: 10px; }
  .offer-title { left: 30px; top: 283px; font-size: 16px; font-weight: 700; color: var(--navy); }
  .offer-list { list-style: none; font-size: 15px; color: var(--ink); }
  .offer-list li { display: flex; align-items: center; gap: 9px; height: 26px; }
  .offer-list--a { left: 30px; top: 313px; }
  .offer-list--b { left: 257px; top: 316px; }
  .photo { top: 418px; width: 198px; height: 106px; border: 2px solid var(--gold); }
  .photo--car { left: 28px; background: linear-gradient(160deg, #8fa0b6, #4c5d78 55%, #9a4242); }
  .photo--ramp { left: 238px; background: linear-gradient(160deg, #c9c7c1, #a9a9a6 55%, #7a7a76); }
  .web-back { left: 32px; top: 564px; font-size: 16px; font-weight: 700; letter-spacing: 3px; color: var(--ink); }
  .brand-back { left: 508px; top: 100px; font-size: 14px; letter-spacing: 2px; color: var(--navy); }
  .stamp { left: 744px; top: 87px; width: 50px; height: 53px; border: 2px dashed #bdbdbd; }
  .address-line { left: 513px; width: 290px; height: 1px; background: #555; }
  .contact-title { left: 512px; top: 444px; font-size: 16px; font-weight: 700; color: var(--navy); }
  .contact-list { left: 512px; top: 480px; list-style: none; font-size: 14.5px; color: var(--ink); }
  .contact-list li { display: flex; gap: 11px; align-items: flex-start; line-height: 17px; margin-bottom: 8px; }
  .contact-list svg { flex: none; margin-top: 2px; }
</style>
</head>
<body>
<div class="canvas">

  <section class="card card--front">
    <svg class="shapes" width="838" height="605" viewBox="0 0 838 605">
      <polygon points="0,0 838,0 838,118 498,118 453,212 0,212" fill="var(--navy)"/>
      <polygon points="0,214 455,214 500,120 838,120 838,138 510,138 466,232 0,232" fill="var(--gold)"/>
      <polygon points="228,238 466,238 512,143 572,143 432,420 150,420" fill="var(--navy-deep)"/>
      <polygon points="540,548 838,540 838,546 540,553" fill="var(--navy)"/>
      <polygon points="555,556 838,550 838,605 540,605" fill="var(--gold-light)"/>
      <rect x="0" y="592" width="560" height="13" fill="var(--gold)"/>
    </svg>
    <div class="abs truck-photo" role="img" aria-label="Photo of a white flatbed tow truck carrying a worn sedan"></div>
    <div class="abs serif hero-kicker">Specializing in<br>Towing &amp; Transportation</div>
    <div class="abs serif hero-title">INSURANCE</div>
    <div class="abs serif brand-name">PEMBROOK INSURANCE</div>
    <div class="abs serif welcome-kicker">Welcome to</div>
    <div class="abs serif welcome-name">PEMBROOK INSURANCE</div>
    <p class="abs sans welcome-copy">Welcome to our website! At Pembrook Insurance we are committed to being available to meet the needs of your business. In this site, you will find tools to connect with our agency so no matter the time or day, your business doesn't slow down. Our customers were in mind when developing this site and we will continue to find ways to make doing business with us easy</p>
    <div class="abs serif call-label">CALL US</div>
    <div class="abs call-number">+334-555-0187</div>
    <div class="abs serif web-front">www.pembrookins-example.net</div>
  </section>

  <section class="card card--back">
    <svg class="shapes" width="838" height="605" viewBox="0 0 838 605">
      <polygon points="0,0 838,0 838,20 250,20 236,50 0,50" fill="var(--navy)"/>
      <polygon points="0,52 237,52 251,22 838,22 838,30 256,30 242,60 0,60" fill="var(--gold)"/>
      <rect x="0" y="540" width="440" height="5" fill="var(--navy)"/>
      <polygon points="0,550 460,550 495,605 0,605" fill="var(--gold-light)"/>
      <polygon points="478,585 838,585 838,595 488,595" fill="var(--navy)"/>
      <rect x="488" y="598" width="350" height="7" fill="var(--gold)"/>
    </svg>
    <div class="abs sans intro-panel">
      <p>With our Agency, we work to make ourselves available to your business for when you need us most to keep your business moving forward.</p>
      <p>Our customers were in mind when developing our agency and will continue to find new ways to make doing business with us easier.</p>
    </div>
    <div class="abs serif offer-title">WE OFFER</div>
    <ul class="abs sans offer-list offer-list--a">
      <li><svg width="12" height="12" viewBox="0 0 12 12"><circle cx="6" cy="6" r="5" fill="none" stroke="var(--navy)" stroke-width="1.4"/><path d="M3.5 6.2l1.8 1.8 3.4-3.6" fill="none" stroke="var(--navy)" stroke-width="1.4"/></svg>Dealers Physical Damage</li>
      <li><svg width="12" height="12" viewBox="0 0 12 12"><circle cx="6" cy="6" r="5" fill="none" stroke="var(--navy)" stroke-width="1.4"/><path d="M3.5 6.2l1.8 1.8 3.4-3.6" fill="none" stroke="var(--navy)" stroke-width="1.4"/></svg>Auto Dealer Liability</li>
    </ul>
    <ul class="abs sans offer-list offer-list--b">
      <li><svg width="12" height="12" viewBox="0 0 12 12"><circle cx="6" cy="6" r="5" fill="none" stroke="var(--navy)" stroke-width="1.4"/><path d="M3.5 6.2l1.8 1.8 3.4-3.6" fill="none" stroke="var(--navy)" stroke-width="1.4"/></svg>Garage Liability</li>
      <li><svg width="12" height="12" viewBox="0 0 12 12"><circle cx="6" cy="6" r="5" fill="none" stroke="var(--navy)" stroke-width="1.4"/><path d="M3.5 6.2l1.8 1.8 3.4-3.6" fill="none" stroke="var(--navy)" stroke-width="1.4"/></svg>Garage Repair Liability</li>
    </ul>
    <div class="abs photo photo--car" role="img" aria-label="Photo of a damaged blue sedan loaded on a tow truck"></div>
    <div class="abs photo photo--ramp" role="img" aria-label="Photo of a silver car being hooked onto a tilted flatbed ramp"></div>
    <div class="abs serif web-back">www.pembrookins-example.net</div>
    <div class="abs serif brand-back">PEMBROOK INSURANCE</div>
    <div class="abs stamp"></div>
    <div class="abs address-line" style="top:205px"></div>
    <div class="abs address-line" style="top:240px"></div>
    <div class="abs address-line" style="top:277px"></div>
    <div class="abs address-line" style="top:313px"></div>
    <div class="abs serif contact-title">CONTACT US</div>
    <ul class="abs sans contact-list">
      <li><svg width="12" height="14" viewBox="0 0 12 14"><path d="M6 1a4 4 0 0 1 4 4c0 3-4 7-4 7S2 8 2 5a4 4 0 0 1 4-4z" fill="none" stroke="var(--navy)" stroke-width="1.4"/><circle cx="6" cy="5" r="1.4" fill="var(--navy)"/></svg><span>718 Hollis Row NW, Suite F Decatur,<br>AL 35988</span></li>
      <li><svg width="12" height="12" viewBox="0 0 12 12"><rect x="1" y="3" width="10" height="7" fill="var(--navy)"/><path d="M1 3l5 4 5-4" fill="none" stroke="#fff" stroke-width="1"/></svg><span>PembrookInfo@velmarlink.example</span></li>
      <li><svg width="12" height="12" viewBox="0 0 12 12"><path d="M2.5 1.5l2 0 1 2.5-1.3 1a6 6 0 0 0 2.8 2.8l1-1.3 2.5 1v2a1 1 0 0 1-1 1A9 9 0 0 1 1.5 2.5a1 1 0 0 1 1-1z" fill="var(--navy)"/></svg><span>+334-555-0187</span></li>
    </ul>
  </section>

</div>
</body>
</html>
```